Brightpath Holdings Business Card

Create a two sided, high gloss, quality business card for Brightpath Holdings.

Target Market(s)

People wanting to purchase, scale, and sell businesses.

Industry/Entity Type

Entrepreneurs

Contact Information for Business Card

One line: Dana Corwell, CPA, CMA Another line: Entrepreneur & Investor Another line: Business Ownership Transition Expert Another line: Multi-State Licensed Real Estate Broker Phone 954-BRTPATH (278-7284) Email Dana@Brightpath Holdings.com Website www.Brightpath.com

Requirements
Must have
• Black Card, logo on one side, all other information on the other side including a small logo.
Nice to have
• Possibly add a tagline "Helping entrepreneurs live a life they don't need a vacation from"
Should not have
• There will not be a mailing address on these cards.

```html
<!DOCTYPE html>
<html lang="en">
<head>
<meta charset="utf-8">
<title>Brightpath Holdings – Business Card</title>
<link rel="stylesheet" href="https://fonts.googleapis.com/css2?family=Montserrat:wght@400;700&display=swap">
<style>
  :root {
    --page: #ffffff;
    --card: #070808;
    --ink: #ffffff;
    --gold: #d6b14c;
  }
  * { margin: 0; padding: 0; box-sizing: border-box; }
  html, body { width: 1200px; height: 848px; overflow: hidden; background: var(--page); }
  body { position: relative; font-family: "Montserrat", Arial, sans-serif; color: var(--ink); }

  .card {
    position: absolute;
    left: 297px;
    width: 583px;
    height: 333px;
    background: var(--card);
    overflow: hidden;
  }
  .card--front { top: 68px; }
  .card--back { top: 431px; }

  .name {
    position: absolute; left: 24px; top: 69px;
    font-size: 29px; font-weight: 400; line-height: 1; white-space: nowrap;
  }
  .name strong { font-weight: 700; }
  .role {
    position: absolute; left: 24px; top: 103px;
    font-size: 16px; letter-spacing: 0.3px;
  }
  .specialty {
    position: absolute; top: 154px;
    font-size: 21px; line-height: 25px; letter-spacing: 0.4px;
  }
  .specialty--left { left: 24px; }
  .specialty--right { left: 345px; }
  .specialty-divider {
    position: absolute; left: 291px; top: 167px;
    width: 2px; height: 35px; background: var(--ink);
  }
  .rule {
    position: absolute; left: 23px; top: 224px;
    width: 537px; height: 2px; background: var(--ink);
  }
  .contact {
    position: absolute; left: 24px; top: 244px;
    font-size: 16px; line-height: 20.5px; white-space: nowrap;
  }
  .contact-row { display: flex; }
  .contact-label { font-weight: 700; width: 87px; }

  .brand {
    position: absolute; display: flex; align-items: center;
    color: var(--gold); font-weight: 700;
  }
  .brand-dot { border-radius: 50%; background: var(--gold); flex: none; }
  .brand-name { line-height: 1.05; }

  .brand--small { right: 23px; top: 247px; gap: 8px; font-size: 20px; text-align: right; }
  .brand--small .brand-dot { width: 12px; height: 12px; }

  .brand--large { left: 50%; top: 50%; transform: translate(-50%, -50%); gap: 18px; font-size: 46px; }
  .brand--large .brand-dot { width: 30px; height: 30px; }
</style>
</head>
<body>

<section class="card card--front" aria-label="Business card front">
  <h1 class="name"><strong>Dana Corwell,</strong> CPA, CMA</h1>
  <p class="role">Entrepreneur &amp; Investor</p>

  <p class="specialty specialty--left">Business Ownership<br>Transition Expert</p>
  <span class="specialty-divider"></span>
  <p class="specialty specialty--right">Multi-State Licensed<br>Real Estate Broker</p>

  <span class="rule"></span>

  <div class="contact">
    <div class="contact-row"><span class="contact-label">Phone:</span><span>954-BRTPATH (278-7284)</span></div>
    <div class="contact-row"><span class="contact-label">Email:</span><span>Dana@Brightpath Holdings.com</span></div>
    <div class="contact-row"><span class="contact-label">Website:</span><span>www.Brightpath.com</span></div>
  </div>

  <div class="brand brand--small">
    <span class="brand-dot"></span>
    <span class="brand-name">Brightpath<br>Holdings</span>
  </div>
</section>

<section class="card card--back" aria-label="Business card back">
  <div class="brand brand--large">
    <span class="brand-dot"></span>
    <span class="brand-name">Brightpath<br>Holdings</span>
  </div>
</section>

</body>
</html>
```